An innovative software company needs a business card!

We need a business card design for our new innovative software company. Please use the details for the business card provided in business card details section. We will use the business card paper like: https://www.plavex.com/us/products/nfc/business-cards-plus.html Our company name: kelvora We have already a logo and colors to use in business cards too ,

Target Market(s)

App & Sofware Development

Industry/Entity Type

Software

Contact Information for Business Card

Lukas Brenner, BSc.
Owner and Creative Superhero

Adress:
Tulpenweg 37/4/1809
A - 1100, Wien

Tel: +43 (0) 676 921 35 60
Email: lukas.brenner@kelvora.at
Web: www.kelvora.at

Requirements
Must have
• - Use our logo
Nice to have
• It would be nice to have a nice picture on the backside. (About apps, software, technicals or funy stuff) - Use our colors as in business card (optional)

```html
<!DOCTYPE html>
<html lang="de">
<head>
<meta charset="utf-8">
<title>kelvora – Visitenkarte</title>
<link rel="stylesheet" href="https://fonts.googleapis.com/css2?family=Ubuntu:wght@400;500;700&display=swap">
<style>
  :root {
    --page-bg: #c9cdd0;
    --card-white: #f7f7f6;
    --brand-blue: #1e9fd4;
    --back-blue: #1ea5d2;
    --art-light: #6cc3e6;
    --art-mid: #4fb2dc;
    --art-navy: #1d3350;
    --text-dark: #3f3f3f;
    --mark-grey: #c9ccd0;
    --watermark: #e3eaf0;
  }
  * { box-sizing: border-box; margin: 0; padding: 0; }
  html, body { width: 1055px; height: 1200px; overflow: hidden; }
  body {
    background: var(--page-bg);
    font-family: "Ubuntu", sans-serif;
    position: relative;
  }
  .card {
    position: absolute;
    left: 202px;
    width: 650px;
    height: 404px;
    overflow: hidden;
  }
  .card-front { top: 170px; background: var(--card-white); }
  .card-back { top: 649px; height: 380px; background: var(--back-blue); }

  .front-watermark {
    position: absolute;
    left: 354px;
    top: -2px;
    width: 440px;
    height: 440px;
    border-radius: 50%;
    background: var(--watermark);
  }

  .brand {
    position: absolute;
    left: 22px;
    top: 62px;
    display: flex;
    align-items: center;
    gap: 26px;
  }
  .brand-dot {
    width: 88px;
    height: 88px;
    border-radius: 50%;
    background: var(--mark-grey);
  }
  .brand-name {
    font-weight: 700;
    font-size: 66px;
    line-height: 1;
    color: var(--brand-blue);
    letter-spacing: 1px;
  }

  .person { position: absolute; left: 32px; top: 178px; }
  .person-name {
    font-weight: 500;
    font-size: 21px;
    letter-spacing: 1.8px;
    color: var(--brand-blue);
    text-transform: uppercase;
    line-height: 1.1;
  }
  .person-role {
    font-size: 19.5px;
    color: var(--text-dark);
    line-height: 1.15;
  }

  .address {
    position: absolute;
    left: 32px;
    top: 237px;
    font-size: 19.5px;
    line-height: 20px;
    color: var(--text-dark);
    font-style: normal;
  }

  .contacts {
    position: absolute;
    left: 28px;
    top: 296px;
    list-style: none;
    font-size: 19.5px;
    line-height: 20px;
    color: var(--text-dark);
  }
  .contacts li { display: flex; align-items: center; gap: 10px; height: 20px; }
  .contacts svg { width: 16px; height: 16px; flex: none; }

  .back-art {
    position: absolute;
    left: 118px;
    top: 8px;
    width: 450px;
    height: 362px;
    border-radius: 28px;
    background: linear-gradient(180deg, var(--art-light) 0%, var(--art-mid) 55%, var(--art-navy) 100%);
  }
</style>
</head>
<body>
  <section class="card card-front" aria-label="Vorderseite">
    <div class="front-watermark" aria-hidden="true"></div>

    <div class="brand">
      <span class="brand-dot"></span>
      <span class="brand-name">kelvora</span>
    </div>

    <div class="person">
      <p class="person-name">Lukas Brenner, BSc.</p>
      <p class="person-role">Owner and Creative Superhero</p>
    </div>

    <address class="address">
      Tulpenweg 37/4/1809<br>
      A - 1100, Wien
    </address>

    <ul class="contacts">
      <li>
        <svg viewBox="0 0 16 16" aria-hidden="true"><rect x="0" y="0" width="16" height="16" rx="3" fill="#1e9fd4"/><path d="M5 3.5c.6 0 1.5 2 1.5 2.4 0 .5-.9.9-.9 1.3 0 .8 2.1 2.9 2.9 2.9.4 0 .8-.9 1.3-.9.4 0 2.4.9 2.4 1.5 0 1-1.3 1.9-2.2 1.9C7.2 12.6 3.4 8.8 3.4 5.8c0-.9.9-2.3 1.6-2.3z" fill="#fff"/></svg>
        <span>+43 (0) 676 921 35 60</span>
      </li>
      <li>
        <svg viewBox="0 0 16 16" aria-hidden="true"><rect x="0.5" y="3" width="15" height="10" fill="#1e9fd4"/><path d="M1 3.5l7 5 7-5M1 12.5l5-4.5M15 12.5l-5-4.5" stroke="#fff" stroke-width="1" fill="none"/></svg>
        <span>lukas.brenner@kelvora.at</span>
      </li>
      <li>
        <svg viewBox="0 0 16 16" aria-hidden="true"><g fill="none" stroke="#1e9fd4" stroke-width="1.2"><circle cx="8" cy="8" r="7"/><ellipse cx="8" cy="8" rx="3" ry="7"/><path d="M1 8h14M2.2 4.5h11.6M2.2 11.5h11.6"/></g></svg>
        <span>www.kelvora.at</span>
      </li>
    </ul>
  </section>

  <section class="card card-back" aria-label="Rückseite">
    <div class="back-art" role="img" aria-label="Illustration: sechs Personen sitzen an einem Besprechungstisch, darüber eine gelbe Glühbirne mit Gehirn und vernetzte Software-Symbole wie Wolken, Zahnräder, Uhr und Diagramm"></div>
  </section>
</body>
</html>
```